Cobalt Ridge Sports Autographed Helmet

I need a Label for an autographed helmet box that has my Cobalt Ridge sports logo on it. It is a box that has a helmet in it that no one knows whos in side and alot of people bid on it to hope to get the team that comes out to get the box. The label needs to have Cobalt Ridge Sports logo with Autographed Helmet on it. I like the gold leaf look the most and use it the most with my business. I am open and would like to have something classy yet creative logo.

Target Market(s)

Sports Memorabilia Collectors

Font styles to use
Sans Serif

Colors

Designer to choose colors to be used in the design.

Requirements
Must have
• My Cobalt Ridge Sports Logo
Should not have
• No Question Marks or Mystery feels
• Shouldnt be any team specified helmets on the box or generic branded helmets with a specific color.

```html
<!DOCTYPE html>
<html lang="en">
<head>
<meta charset="utf-8">
<title>Cobalt Ridge Sports – Autographed Helmet Label</title>
<link rel="stylesheet" href="https://fonts.googleapis.com/css2?family=Bebas+Neue&family=Oswald:wght@600;700&family=Mrs+Saint+Delafield&display=swap">
<style>
  :root {
    --paper: #ffffff;
    --gold: #f2bb33;
    --gold-deep: #d9a22a;
    --charcoal: #3d3d3d;
    --ink: #1f1f1f;
    --tan: #c1ad86;
  }
  html, body {
    margin: 0;
    padding: 0;
    overflow: hidden;
    background: var(--paper);
  }
  .label {
    position: relative;
    width: 1200px;
    height: 911px;
    overflow: hidden;
    background: var(--paper);
  }
  .label__art {
    position: absolute;
    inset: 0;
    width: 1200px;
    height: 911px;
  }
  .band--gold { fill: var(--gold); }
  .band--charcoal { fill: var(--charcoal); }
  .band--tan { fill: var(--tan); }
  .emblem__disc { fill: var(--paper); }
  .emblem__name {
    font-family: "Oswald", sans-serif;
    font-weight: 700;
    fill: var(--gold-deep);
    letter-spacing: 2px;
  }
  .title {
    font-family: "Bebas Neue", sans-serif;
    font-size: 104px;
  }
  .title__shadow { fill: var(--ink); }
  .title__face { fill: var(--gold); }
  .title__rule { fill: var(--tan); }
  .subtitle__script {
    font-family: "Mrs Saint Delafield", cursive;
    font-size: 58px;
    fill: var(--ink);
  }
  .subtitle__word {
    font-family: "Oswald", sans-serif;
    font-weight: 700;
    font-size: 50px;
    letter-spacing: 3px;
  }
  .subtitle__word-shadow { fill: var(--gold); }
  .subtitle__word-face { fill: var(--ink); }
</style>
</head>
<body>
<main class="label">
  <svg class="label__art" viewBox="0 0 1200 911" xmlns="http://www.w3.org/2000/svg">
    <!-- corner accents -->
    <path class="band--charcoal" d="M0 0 H190 Q70 40 0 168 Z"/>
    <path class="band--charcoal" d="M1005 911 Q1140 850 1200 690 L1200 911 Z"/>

    <!-- upper right swoosh -->
    <path class="band--gold" d="M728 208 Q930 80 1100 4 L1185 4 Q960 125 780 285 Z"/>
    <path class="band--charcoal" d="M790 300 Q990 125 1200 22 L1200 145 Q1000 225 800 362 Z"/>

    <!-- lower left swoosh -->
    <path class="band--tan" d="M0 730 Q170 590 335 452 L350 505 Q190 705 78 911 L0 911 Z"/>
    <path class="band--gold" d="M362 520 Q215 700 78 911 L350 911 Q420 760 492 622 Z"/>
    <path class="band--charcoal" d="M502 620 L542 620 Q470 700 420 786 Q452 700 502 620 Z"/>

    <!-- emblem -->
    <circle class="emblem__disc" cx="563" cy="386" r="213"/>
    <text class="emblem__name" x="563" y="395" font-size="64" text-anchor="middle">COBALT RIDGE</text>
    <text class="emblem__name" x="563" y="470" font-size="64" text-anchor="middle">SPORTS</text>

    <!-- title -->
    <g class="title">
      <text class="title__shadow" x="501" y="777" textLength="626" lengthAdjust="spacingAndGlyphs">COBALT RIDGE SPORTS</text>
      <text class="title__face" x="495" y="771" textLength="626" lengthAdjust="spacingAndGlyphs">COBALT RIDGE SPORTS</text>
    </g>
    <rect class="title__rule" x="509" y="784" width="655" height="5"/>

    <!-- subtitle -->
    <text class="subtitle__script" x="584" y="850">Autographed</text>
    <g class="subtitle__word">
      <text class="subtitle__word-shadow" x="812" y="846" textLength="146" lengthAdjust="spacingAndGlyphs">HELMET</text>
      <text class="subtitle__word-face" x="809" y="843" textLength="146" lengthAdjust="spacingAndGlyphs">HELMET</text>
    </g>
  </svg>
</main>
</body>
</html>
```